Wordpress site needed for company's Healthcare Web App

Healthcare web app needs wordpress web design for web site that provides an overview of the product, a page explaining key features, a blog, a press release announcement section, customer testimonials, contact us, sign up page, invite friends.

The website should use the color scheme including in the logo. This web site is not the app, this website will be used to introduce the app.

Target Market(s)

Doctors, enterprise healthcare professionals, patients who will use patient portals to access their health info. (not the app itself, but this site introduces the app)

Industry/Entity Type

Health Care

Coding

Coded - Design and coding required

Number of Pages Required

5+ page

Font styles to use
Sans Serif

Requirements
Must have
• This is a Wordpress based site.
• Product Overview, Key Product Features, Blog, Press Releases, Events, Embedded Videos explaining the product and demo'ing features, Sign Up Page for people interested,
Nice to have
• Uplifting Hero Image for Healthcare Tech, color scheme fitting with logo

```html
<!DOCTYPE html>
<html lang="en">
<head>
<meta charset="utf-8">
<title>CareLedger — Record-keeping App</title>
<link rel="stylesheet" href="https://fonts.googleapis.com/css2?family=Lato:ital,wght@0,400;0,700;0,900;1,400;1,700&display=swap">
<style>
:root{
  --teal:#1b8aa8;
  --teal-dark:#177590;
  --band:#1f7f99;
  --ink:#2b2b2b;
  --muted:#555;
  --heading:#5a5a5a;
  --cream:#f3f1e8;
  --cream-2:#e9e7dc;
  --night:#06152b;
  --white:#fff;
}
*{box-sizing:border-box;margin:0;padding:0}
html,body{width:1200px;height:3103px;overflow:hidden}
body{font-family:'Lato',sans-serif;color:var(--ink);background:var(--cream);position:relative}
section,header,footer{position:absolute;left:0;width:1200px}
.abs{position:absolute}
.placeholder{position:absolute}

/* hero */
.hero{top:0;height:571px;overflow:hidden}
.hero-bg{inset:0;background:radial-gradient(ellipse at 45% 45%,#2a7ec4 0%,#124a86 35%,#061a3a 75%,#030c1d 100%)}
.topbar{position:absolute;top:0;left:0;width:1200px;height:86px;background:rgba(2,10,24,.55);border-bottom:1px solid rgba(255,255,255,.12)}
.brand{position:absolute;left:161px;top:22px;display:flex;align-items:center;gap:10px;color:var(--white);font-weight:700;font-size:30px}
.brand-dot{width:34px;height:34px;border-radius:50%;background:var(--white)}
.nav{position:absolute;top:32px;left:495px;display:flex;gap:22px;align-items:center;font-size:14px;color:var(--white)}
.nav .btn-line{border:1.5px solid var(--white);border-radius:3px;padding:3px 10px}
.nav .auth{display:flex;gap:12px;margin-left:6px}
.hero-title{left:163px;top:252px;color:var(--white);font-size:35px;line-height:37px;font-weight:400}
.hero-title b{font-weight:900}
.cta{left:163px;top:451px;width:190px;height:50px;background:var(--teal);border:2px solid rgba(255,255,255,.8);color:var(--white);font-weight:700;font-size:17px;display:flex;align-items:center;justify-content:center}
.hero-device{left:600px;top:93px;width:560px;height:478px;background:linear-gradient(135deg,#d8dde2,#9fa8b0 60%,#d6b79c);border-radius:40px 40px 0 0;opacity:.9}

/* headings */
.sec-title{font-size:37px;font-weight:400;color:var(--heading)}
.sec-title span{color:var(--teal)}
.heart{display:block;width:22px;height:18px;margin-top:4px}
.center{left:0;width:1200px;text-align:center}
.center .heart{margin:4px auto 0}

/* about */
.about{top:571px;height:401px;background:var(--cream)}
.about .sec-title{left:163px;top:68px}
.about .heart{position:absolute;left:163px;top:117px}
.about-text{left:163px;top:145px;width:460px;font-size:11.5px;line-height:15px;color:var(--ink)}
.readmore{left:163px;top:283px;font-size:15px;color:var(--teal);text-decoration:underline;display:flex;gap:6px;align-items:center}
.about-art{left:631px;top:46px;width:455px;height:324px;background:linear-gradient(135deg,#e8efe6,#9bd36a 45%,#2a6fb5 80%,#e2e5ea);border-radius:12px;opacity:.85}

/* features */
.features{top:972px;height:524px;background:var(--cream-2)}
.features .sec-title{top:44px}
.phone-art{left:445px;top:145px;width:310px;height:379px;background:linear-gradient(180deg,#2f3338 0%,#2b9bb3 30%,#35a6bd 65%,#e9b27e 100%);border-radius:30px 30px 0 0}
.feat{position:absolute;width:300px}
.feat h3{font-size:14px;font-weight:400;color:var(--teal);line-height:16px}
.feat p{font-size:11.5px;line-height:15px;color:var(--ink)}
.feat.left{left:48px;text-align:right}
.feat.right{left:834px}
.ficon{position:absolute;width:48px;height:48px;background:var(--white);border:1px solid #d6d3c7;display:flex;align-items:center;justify-content:center}
.ficon.left{left:362px}
.ficon.right{left:776px}
.connector{position:absolute;height:1px;background:#b9b7ad}

/* demo */
.demo{top:1496px;height:521px;background:var(--cream)}
.demo .sec-title{top:40px}
.tablet-art{left:248px;top:128px;width:704px;height:393px;background:linear-gradient(180deg,#1a1a1a 0%,#bfc7cc 12%,#d3d8db 60%,#e3c3a6 100%);border-radius:22px 22px 0 0}

/* testimonials */
.testimonials{top:2017px;height:404px;background:var(--cream-2)}
.testimonials .sec-title{top:34px}
.quote{left:200px;top:135px;width:800px;font-size:11.5px;line-height:21px;font-style:italic;text-align:center;color:var(--ink)}
.quote .mark{font-weight:900;font-size:22px;font-style:normal;color:#222;vertical-align:-4px;margin:0 6px}
.author{top:222px;font-size:13px;font-weight:700;font-style:italic}
.avatar{left:569px;top:259px;width:62px;height:62px;background:linear-gradient(180deg,#c9d6e6,#1f3553);border:3px solid var(--teal)}
.dots{top:337px;display:flex;justify-content:center;gap:6px}
.dots i{width:7px;height:7px;border-radius:50%;background:#9fb7c1;display:block}
.dots i:first-child{background:var(--teal)}

/* blog & news */
.updates{top:2421px;height:430px;background:var(--cream)}
.updates .sec-title{top:42px}
.blog-title{left:166px}
.news-title{left:627px}
.updates .heart.l{position:absolute;left:166px;top:92px}
.updates .heart.r{position:absolute;left:627px;top:92px}
.rule{position:absolute;height:1px;background:#d4d1c4;top:100px}
.post-img{width:140px;height:104px;border:4px solid var(--white);box-shadow:0 0 0 1px #d4d1c4}
.date-badge{position:absolute;width:32px;height:26px;background:var(--teal);color:var(--white);font-size:10px;font-weight:700;line-height:11px;text-align:center;padding-top:2px}
.post-body{position:absolute;width:238px}
.post-body h4{font-size:13px;font-weight:700;margin-bottom:8px}
.post-body p{font-size:10.5px;line-height:14.5px}
.news-date{position:absolute;width:56px;height:62px;border:1px solid #cfccbf;background:var(--white);text-align:center}
.news-date .m{background:var(--teal);color:var(--white);font-size:11px;font-weight:700;height:18px;line-height:18px}
.news-date .d{font-size:26px;font-weight:700;line-height:42px}
.news-body{position:absolute;width:336px}
.news-body h4{font-size:13px;font-weight:700;margin-bottom:4px}
.news-body p{font-size:10.5px;line-height:14.5px}
.news-body p span{color:var(--teal)}
.news-sep{position:absolute;left:627px;width:410px;height:1px;background:#dcd9cc}

/* signup */
.signup{top:2851px;height:205px;background:var(--band)}
.signup h2{top:38px;font-size:27px;font-weight:400;color:var(--white)}
.signup .sub{top:72px;font-size:10px;font-style:italic;font-weight:700;color:var(--white)}
.field{position:absolute;top:108px;height:37px;background:var(--white);font-size:10px;color:#999;font-style:italic;padding:12px 10px}
.submit{position:absolute;top:108px;left:838px;width:110px;height:37px;background:#1e2a2f;color:var(--white);font-size:13px;font-weight:700;display:flex;align-items:center;justify-content:center}

footer{top:3056px;height:47px;background:var(--cream);border-top:1px solid #dedbd0}
.copyright{position:absolute;left:161px;top:18px;font-size:10px;color:var(--muted)}
.foot-brand{position:absolute;left:912px;top:11px;display:flex;gap:6px;align-items:center;font-size:18px;font-weight:700;color:var(--teal)}
.foot-brand i{width:20px;height:20px;border-radius:50%;background:var(--teal);display:block}
</style>
</head>
<body>

<header class="hero">
  <div class="placeholder hero-bg" role="img" aria-label="Blue glowing digital healthcare technology background"></div>
  <div class="topbar">
    <div class="brand"><span class="brand-dot"></span>CareLedger</div>
    <nav class="nav">
      <span>Home</span><span>About Apps</span><span>Features</span><span>Blog</span><span>Press</span><span>Contact Us</span>
      <span class="auth"><span class="btn-line">Sign Up</span><span class="btn-line">Log In</span></span>
    </nav>
  </div>
  <h1 class="abs hero-title">Comprehensive<br><b>Record-keeping App</b> For<br>Your <b>Personal Medical<br>Information.</b></h1>
  <svg class="abs" style="left:360px;top:380px" width="60" height="70" viewBox="0 0 60 70"><path d="M45 5 C60 30 45 55 15 58" fill="none" stroke="#fff" stroke-width="4"/><path d="M22 48 L10 58 L24 66" fill="none" stroke="#fff" stroke-width="4"/></svg>
  <div class="abs cta">Download App Now</div>
  <div class="placeholder hero-device" role="img" aria-label="Hand holding a smartphone showing the app start screen"></div>
</header>

<section class="about">
  <h2 class="abs sec-title">About <span>CareLedger</span></h2>
  <svg class="heart" viewBox="0 0 22 18"><path d="M11 16 C3 10 1 7 1 5 a5 5 0 0 1 10 -1 a5 5 0 0 1 10 1 c0 2 -2 5 -10 11z" fill="none" stroke="#1b8aa8" stroke-width="1.6"/></svg>
  <p class="abs about-text">Lorem ipsum dolor sit amet, consectetuer adipiscing elit, sed diam nonummy nibh euismod tincidunt ut laoreet dolore magna aliquam erat volutpat. Ut wisi enim ad minim veniam, quis nostrud exerci tation ullamcorper suscipit lobortis nisl ut aliquip ex ea commodo consequat. Duis autem vel eum iriure dolor in hendrerit in vulputate velit esse molestie consequat, vel illum dolore eu feugiat nulla facilisis at vero eros et accumsan et iusto odio dignissim qui blandit praesent luptatum zzril delenit augue duis dolore te feugait nulla facilisi. Ut wisi enim ad minim veniam, quis nostrud exerci tation ullamcorper suscipit lobortis nisl ut aliquip ex ea commodo consequat.</p>
  <div class="abs readmore"><svg width="16" height="12" viewBox="0 0 16 12"><path d="M1 6 H14 M9 1 L14 6 L9 11" fill="none" stroke="#1b8aa8" stroke-width="1.6"/></svg>Read More</div>
  <div class="placeholder about-art" role="img" aria-label="Illustration of a stethoscope, laptop, phone, tablet and medical items"></div>
</section>

<section class="features">
  <h2 class="abs center sec-title">App <span>Features</span></h2>
  <svg class="heart abs" style="left:589px;top:92px" viewBox="0 0 22 18"><path d="M11 16 C3 10 1 7 1 5 a5 5 0 0 1 10 -1 a5 5 0 0 1 10 1 c0 2 -2 5 -10 11z" fill="none" stroke="#1b8aa8" stroke-width="1.6"/></svg>
  <div class="placeholder phone-art" role="img" aria-label="Illustrated hand holding a phone with the app's feature icons and a download button"></div>

  <div class="feat left" style="top:130px"><h3>It's for the whole family</h3><p>Lorem ipsum dolor sit amet,<br>consectetuer piscing .</p></div>
  <div class="feat left" style="top:225px"><h3>A medical record and more</h3><p>Lorem ipsum dolor sit amet,<br>consectetuer piscing .</p></div>
  <div class="feat left" style="top:322px"><h3>A digital file cabinet</h3><p>Lorem ipsum dolor sit amet,<br>consectetuer piscing .</p></div>
  <div class="feat left" style="top:410px"><h3>Chart test results with<br>sophistication</h3><p>Lorem ipsum dolor sit amet,<br>consectetuer piscing .</p></div>

  <div class="feat right" style="top:130px"><h3>21st century record-keeping</h3><p>Lorem ipsum dolor sit amet,<br>consectetuer piscing .</p></div>
  <div class="feat right" style="top:225px"><h3>Works with your calendar</h3><p>Lorem ipsum dolor sit amet,<br>consectetuer piscing .</p></div>
  <div class="feat right" style="top:322px"><h3>From blood tests to X-rays</h3><p>Lorem ipsum dolor sit amet,<br>consectetuer piscing .</p></div>
  <div class="feat right" style="top:428px"><h3>Have a long medical history</h3><p>Lorem ipsum dolor sit amet,<br>consectetuer piscing .</p></div>

  <div class="ficon left" style="top:131px"><svg width="26" height="22" viewBox="0 0 26 22"><circle cx="8" cy="6" r="4" fill="#1b8aa8"/><circle cx="18" cy="6" r="4" fill="#1b8aa8"/><rect x="2" y="12" width="12" height="9" rx="3" fill="#1b8aa8"/><rect x="12" y="12" width="12" height="9" rx="3" fill="#1b8aa8"/></svg></div>
  <div class="ficon left" style="top:226px"><svg width="20" height="24" viewBox="0 0 20 24"><rect x="2" y="3" width="16" height="20" fill="none" stroke="#1b8aa8" stroke-width="2"/><path d="M6 10h8M6 14h8M6 18h5" stroke="#1b8aa8" stroke-width="2"/></svg></div>
  <div class="ficon left" style="top:323px"><svg width="26" height="20" viewBox="0 0 26 20"><rect x="1" y="4" width="24" height="15" fill="#1b8aa8"/><path d="M13 7v9M8.5 11.5h9" stroke="#fff" stroke-width="2.5"/></svg></div>
  <div class="ficon left" style="top:420px"><svg width="24" height="22" viewBox="0 0 24 22"><path d="M2 20h20" stroke="#1b8aa8" stroke-width="2"/><rect x="4" y="10" width="3" height="9" fill="#1b8aa8"/><rect x="10" y="5" width="3" height="14" fill="#1b8aa8"/><rect x="16" y="8" width="3" height="11" fill="#1b8aa8"/></svg></div>

  <div class="ficon right" style="top:131px"><svg width="20" height="24" viewBox="0 0 20 24"><rect x="2" y="2" width="16" height="20" fill="#1b8aa8"/><path d="M6 8h8M6 12h8M6 16h8" stroke="#fff" stroke-width="2"/></svg></div>
  <div class="ficon right" style="top:226px"><svg width="24" height="22" viewBox="0 0 24 22"><rect x="2" y="3" width="20" height="18" fill="none" stroke="#1b8aa8" stroke-width="2"/><path d="M2 8h20M7 12h2M11 12h2M15 12h2M7 16h2M11 16h2" stroke="#1b8aa8" stroke-width="2"/></svg></div>
  <div class="ficon right" style="top:323px"><svg width="24" height="24" viewBox="0 0 24 24"><path d="M4 20 L16 8 M14 4 L20 10 M11 9 l4 4" stroke="#1b8aa8" stroke-width="2.5"/></svg></div>
  <div class="ficon right" style="top:420px"><svg width="20" height="24" viewBox="0 0 20 24"><rect x="2" y="2" width="16" height="20" fill="#1b8aa8"/><path d="M6 8h8M6 12h8M6 16h8" stroke="#fff" stroke-width="2"/></svg></div>

  <div class="connector" style="left:410px;top:155px;width:70px"></div>
  <div class="connector" style="left:410px;top:250px;width:50px"></div>
  <div class="connector" style="left:410px;top:347px;width:40px"></div>
  <div class="connector" style="left:410px;top:444px;width:40px"></div>
  <div class="connector" style="left:720px;top:155px;width:56px"></div>
  <div class="connector" style="left:740px;top:250px;width:36px"></div>
  <div class="connector" style="left:745px;top:347px;width:31px"></div>
  <div class="connector" style="left:745px;top:444px;width:31px"></div>
</section>

<section class="demo">
  <h2 class="abs center sec-title">App <span>Demonstration</span></h2>
  <svg class="heart abs" style="left:589px;top:88px" viewBox="0 0 22 18"><path d="M11 16 C3 10 1 7 1 5 a5 5 0 0 1 10 -1 a5 5 0 0 1 10 1 c0 2 -2 5 -10 11z" fill="none" stroke="#1b8aa8" stroke-width="1.6"/></svg>
  <div class="placeholder tablet-art" role="img" aria-label="Hands holding a tablet showing the embedded app demonstration video"></div>
</section>

<section class="testimonials">
  <h2 class="abs center sec-title">User <span>Testimonials</span></h2>
  <svg class="heart abs" style="left:589px;top:82px" viewBox="0 0 22 18"><path d="M11 16 C3 10 1 7 1 5 a5 5 0 0 1 10 -1 a5 5 0 0 1 10 1 c0 2 -2 5 -10 11z" fill="none" stroke="#1b8aa8" stroke-width="1.6"/></svg>
  <p class="abs quote"><span class="mark">&ldquo;</span>Lorem ipsum dolor sit amet, consectetur adipiscing elit, sed do eiusmod tempor incididunt ut labore et dolore magna aliqua. Ut enim veniam, quis nostrud exercitation ullamco laboris nisi ut aliquip ex ea commodo consequat. Duis aute irure dolor in reprehenderit in voluptate velit esse cillum dolore eu fugiat nulla pariatur. Excepteur sint occaecat cupidatat non proident, sunt in culpa qui officia .<span class="mark">&rdquo;</span></p>
  <p class="abs center author">- Sconsectetur adipiscing</p>
  <div class="placeholder avatar" role="img" aria-label="Portrait photo of the reviewer"></div>
  <div class="abs center dots"><i></i><i></i><i></i></div>
</section>

<section class="updates">
  <h2 class="abs sec-title blog-title">Latest <span>Blog</span></h2>
  <h2 class="abs sec-title news-title">News &amp; <span>Events</span></h2>
  <svg class="heart l" viewBox="0 0 22 18"><path d="M11 16 C3 10 1 7 1 5 a5 5 0 0 1 10 -1 a5 5 0 0 1 10 1 c0 2 -2 5 -10 11z" fill="none" stroke="#1b8aa8" stroke-width="1.6"/></svg>
  <svg class="heart r" viewBox="0 0 22 18"><path d="M11 16 C3 10 1 7 1 5 a5 5 0 0 1 10 -1 a5 5 0 0 1 10 1 c0 2 -2 5 -10 11z" fill="none" stroke="#1b8aa8" stroke-width="1.6"/></svg>
  <div class="rule" style="left:194px;width:378px"></div>
  <div class="rule" style="left:655px;width:382px"></div>

  <div class="placeholder post-img" style="left:166px;top:134px;background:linear-gradient(135deg,#0d2a4a,#4d82b5 55%,#0b1d33)" role="img" aria-label="Blog photo of a digital medical interface"></div>
  <div class="date-badge" style="left:331px;top:134px">27<sup>th</sup><br>Oct</div>
  <div class="post-body" style="left:371px;top:136px"><h4>Lorem ipsum dolor sit amet,</h4></div>
  <div class="post-body" style="left:331px;top:166px"><p>Fusce elementum, nulla vel pellentes consequat, ante nulla hendrerit arcu, ac tincidunt mauris lacus sed leo. vamus suscipit molestie vestibulum. Lorem ipsum dolor sit amet,</p></div>

  <div class="placeholder post-img" style="left:166px;top:275px;background:linear-gradient(135deg,#143b5e,#d88a52 50%,#0c2744)" role="img" aria-label="Blog photo of a hand with glowing health icons"></div>
  <div class="date-badge" style="left:331px;top:275px">25<sup>th</sup><br>Oct</div>
  <div class="post-body" style="left:371px;top:277px"><h4>Lorem ipsum dolor sit amet,</h4></div>
  <div class="post-body" style="left:331px;top:307px"><p>Fusce elementum, nulla vel pellentes consequat, ante nulla hendrerit arcu, ac tincidunt mauris lacus sed leo. vamus suscipit molestie vestibulum. Lorem ipsum dolor sit amet,</p></div>

  <div class="news-date" style="left:627px;top:130px"><div class="m">Nov</div><div class="d">14</div></div>
  <div class="news-body" style="left:699px;top:130px"><h4>Lorem ipsum dolor sit amet,</h4><p>Fusce elementum, nulla vel pellentes consequat, ante nulla hendrerit arcu, ac tincidunt mauris lacus sed leo. vamus suscipit molestie vestibulum. Lorem ipsum dolor sit amet. <span>[+]</span></p></div>
  <div class="news-sep" style="top:207px"></div>
  <div class="news-date" style="left:627px;top:219px"><div class="m">Nov</div><div class="d">12</div></div>
  <div class="news-body" style="left:699px;top:219px"><h4>Lorem ipsum dolor sit amet,</h4><p>Fusce elementum, nulla vel pellentes consequat, ante nulla hendrerit arcu, ac tincidunt mauris lacus sed leo. vamus suscipit molestie vestibulum. Lorem ipsum dolor sit amet. <span>[+]</span></p></div>
  <div class="news-sep" style="top:296px"></div>
  <div class="news-date" style="left:627px;top:308px"><div class="m">Nov</div><div class="d">10</div></div>
  <div class="news-body" style="left:699px;top:308px"><h4>Lorem ipsum dolor sit amet,</h4><p>Fusce elementum, nulla vel pellentes consequat, ante nulla hendrerit arcu, ac tincidunt mauris lacus sed leo. vamus suscipit molestie vestibulum. Lorem ipsum dolor sit amet. <span>[+]</span></p></div>
</section>

<section class="signup">
  <h2 class="abs center">Join our email list</h2>
  <p class="abs center sub">Lorem ipsum dolor sit amet, consectetuer adipiscing elit, sed diam nonummy nibh euismod tincidunt ut laoreet</p>
  <div class="field" style="left:302px;width:263px"></div>
  <div class="field" style="left:571px;width:261px">&#128274; Password</div>
  <div class="submit">SUBMIT</div>
</section>

<footer>
  <p class="copyright">Copyright © 2016 CareLedger. All rights reserved</p>
  <div class="foot-brand"><i></i>CareLedger</div>
</footer>

</body>
</html>
```